business card for a shoe shop

we would like a business card for a family owned shoe shop.
With this information included.
Darnell's Shoe Store
Family owned since 1947

then on other side
Darnell's Shoe Store
Footwear fitting specialist
Phone: 9187 2630
218 Quarry St, Fernleigh Downs 3187
(cnr. Hartwick Rd and Quarry St)
darnellshoes218@examplemail.com
if could incorporate the purple color on card i have attached.

```html
<!DOCTYPE html>
<html lang="en">
<head>
<meta charset="utf-8">
<title>Darnell's Shoe Store – Business Card</title>
<link rel="stylesheet" href="https://fonts.googleapis.com/css2?family=Cinzel:wght@400&family=Poppins:wght@400;600&display=swap">
<style>
  :root {
    --page: #ffffff;
    --violet-deep: #4e0cc2;
    --violet-mid: #6316e8;
    --violet-glow: #8a4cf2;
    --violet-bright: #7019f5;
    --ink-white: #ffffff;
    --frame-dark: #2a0a6a;
    --rule-soft: rgba(255,255,255,0.45);
  }
  * { margin: 0; padding: 0; box-sizing: border-box; }
  html, body { width: 1200px; height: 2377px; overflow: hidden; background: var(--page); }
  .canvas { position: relative; width: 1200px; height: 2377px; }

  .card {
    position: absolute;
    left: 117px;
    width: 966px;
    height: 552px;
    overflow: hidden;
    box-shadow: 0 18px 40px rgba(0,0,0,0.28);
  }
  .card-front {
    top: 600px;
    background: radial-gradient(ellipse 48% 58% at 50% 48%, var(--violet-glow) 0%, var(--violet-mid) 55%, var(--violet-deep) 100%);
  }
  .card-back {
    top: 1225px;
    background: linear-gradient(160deg, var(--violet-mid) 0%, var(--violet-bright) 45%, var(--violet-deep) 100%);
  }

  .brand-square {
    position: absolute;
    border: 1.5px solid var(--frame-dark);
  }
  .brand-name {
    position: absolute;
    font-family: "Cinzel", serif;
    font-weight: 400;
    color: var(--ink-white);
    white-space: nowrap;
    text-align: center;
    line-height: 1;
  }

  /* front */
  .card-front .brand-square { left: 411px; top: 166px; width: 144px; height: 144px; }
  .card-front .brand-name { left: 0; right: 0; top: 318px; font-size: 46px; }
  .tagline {
    position: absolute;
    left: 0; right: 0; top: 364px;
    display: flex; align-items: center; justify-content: center; gap: 16px;
    font-family: "Poppins", sans-serif;
    font-size: 20px;
    color: var(--ink-white);
    letter-spacing: 0.3px;
  }
  .tagline-rule { width: 105px; height: 1px; background: var(--rule-soft); }

  /* back */
  .card-back .brand-square { left: 199px; top: 198px; width: 102px; height: 102px; }
  .card-back .brand-name { left: 50px; width: 396px; top: 307px; font-size: 32px; }
  .divider { position: absolute; left: 476px; top: 131px; width: 1px; height: 286px; background: var(--rule-soft); }

  .role-title {
    position: absolute; left: 509px; top: 145px;
    font-family: "Poppins", sans-serif; font-weight: 600;
    font-size: 35px; line-height: 46px; color: var(--ink-white);
    text-transform: uppercase; letter-spacing: 0.5px;
  }
  .contact-list { position: absolute; left: 507px; top: 272px; list-style: none; }
  .contact-item {
    display: flex; align-items: center; gap: 12px;
    font-family: "Poppins", sans-serif; font-size: 20.5px; line-height: 25px;
    color: var(--ink-white); margin-bottom: 22px;
  }
  .contact-item:nth-child(2) { margin-bottom: 14px; }
  .contact-icon {
    flex: none; width: 32px; height: 32px; border-radius: 4px;
    background: var(--ink-white);
    display: flex; align-items: center; justify-content: center;
  }
  .contact-icon svg { width: 20px; height: 20px; }
</style>
</head>
<body>
<main class="canvas">

  <section class="card card-front" aria-label="Card front">
    <div class="brand-square"></div>
    <h1 class="brand-name">Darnell's Shoe Store</h1>
    <p class="tagline"><span class="tagline-rule"></span>FAMILY OWNED SINCE 1947<span class="tagline-rule"></span></p>
  </section>

  <section class="card card-back" aria-label="Card back">
    <div class="brand-square"></div>
    <h2 class="brand-name">Darnell's Shoe Store</h2>
    <div class="divider"></div>
    <h3 class="role-title">Footwear Fitting<br>Specialist</h3>
    <ul class="contact-list">
      <li class="contact-item">
        <span class="contact-icon">
          <svg viewBox="0 0 24 24" fill="none" stroke="#1a1a1a" stroke-width="2" stroke-linecap="round" stroke-linejoin="round"><path d="M5 3h4l2 5-2.5 1.5a11 11 0 0 0 6 6L16 13l5 2v4a2 2 0 0 1-2 2A16 16 0 0 1 3 5a2 2 0 0 1 2-2z"/></svg>
        </span>
        <span>9187 2630</span>
      </li>
      <li class="contact-item">
        <span class="contact-icon">
          <svg viewBox="0 0 24 24" fill="none" stroke="#1a1a1a" stroke-width="2" stroke-linecap="round" stroke-linejoin="round"><path d="M12 21s-6-5.5-6-11a6 6 0 0 1 12 0c0 5.5-6 11-6 11z"/><circle cx="12" cy="10" r="2.2"/></svg>
        </span>
        <span>218 Quarry St, Fernleigh Downs 3187<br>(cnr. Hartwick Rd and Quarry St)</span>
      </li>
      <li class="contact-item">
        <span class="contact-icon">
          <svg viewBox="0 0 24 24" fill="none" stroke="#1a1a1a" stroke-width="2" stroke-linecap="round" stroke-linejoin="round"><rect x="3" y="6" width="18" height="13" rx="1.5"/><path d="M3 7l9 6 9-6"/></svg>
        </span>
        <span>darnellshoes218@examplemail.com</span>
      </li>
    </ul>
  </section>

</main>
</body>
</html>
```